Creation of a Velmora Flyer design

As part of the cr% 26 # 233; ation of our soci% 26 # 233; t% 26 # 233 ;, we wish to cr% 26 # 233; er a flyer pr% 26 # 233; feeling our diff% 26 # 233; annuities% 26 # 233; s business advisory services% 26 # 233; foreign% 26 # 232; res who wish to develop their activities% 26 # 233; s in Switzerland. We want a double-sided flyer that presents% 26 # 233; society% 26 # 233; t% 26 # 233; d% 26 # 39; a c% 26 # 244; t% 26 # 233; and who presents% 26 # 233; benefits of the other. We have d% 26 # 233; j% 26 # 224; made a very basic provisional flyer to be able to present our activities. We put it to you as an example.

Target Market(s)

European companies% 26 # 233; internal% 26 # 233; res% 26 # 233; es by the market% 26 # 233; Swiss

Industry/Entity Type

Business Consultant

Colors

Designer to choose colors to be used in the design.

Requirements
Must have
• Company name and contact details
A field to detail the services
Nice to have
• Some% 26 # 233; l% 26 # 233; elements that recall Switzerland and some% 26 # 233; l% 26 # 233; elements that recall c% 26 # 244; t% 26 # 233; % 26quot; business% 26quot;

```html
<!DOCTYPE html>
<html lang="en">
<head>
<meta charset="utf-8">
<title>Velmora Flyer</title>
<link href="https://fonts.googleapis.com/css2?family=Questrial&family=Roboto+Condensed:wght@400&display=swap" rel="stylesheet">
<style>
  :root {
    --backdrop: #6b6c6e;
    --brand-blue: #3f73bd;
    --deep-blue: #2f4fa0;
    --brand-purple: #5b3a8e;
    --paper: #eeeef0;
    --paper-low: #d9dadc;
    --ink: #1c1c1e;
    --white: #ffffff;
  }
  * { margin: 0; padding: 0; box-sizing: border-box; }
  html, body { width: 1200px; height: 1200px; overflow: hidden; background: var(--backdrop); }
  .flyer {
    position: absolute; left: 148px; top: 15px; width: 904px; height: 1170px;
    background: linear-gradient(180deg, var(--paper) 40%, var(--paper-low) 100%);
    overflow: hidden;
  }
  .flyer-art { position: absolute; inset: 0; width: 904px; height: 1170px; }
  .brand {
    position: absolute; left: 42px; top: 43px; width: 216px; text-align: center;
    color: var(--white); font-family: "Questrial", sans-serif;
  }
  .brand-square { display: block; width: 52px; height: 50px; margin: 0 auto 12px; background: var(--white); border-radius: 9px; }
  .brand-name { font-size: 33px; letter-spacing: 2px; line-height: 1; }
  .intro {
    position: absolute; left: 48px; top: 432px; width: 410px;
    font-family: "Roboto Condensed", sans-serif; font-size: 25px; line-height: 33.4px;
    color: var(--ink); text-align: justify;
  }
  .headline {
    position: absolute; left: 502px; top: 533px; width: 380px;
    font-family: "Questrial", sans-serif; font-size: 35px; line-height: 41.5px;
    color: var(--brand-blue);
  }
  .body-copy {
    position: absolute; left: 48px; top: 727px; width: 807px;
    font-family: "Roboto Condensed", sans-serif; font-size: 19.5px; line-height: 23.5px;
    color: var(--ink); text-align: justify;
  }
  .body-copy p { margin-bottom: 23px; }
  .footnote {
    position: absolute; left: 48px; top: 999px;
    font-family: "Roboto Condensed", sans-serif; font-size: 13.5px; color: var(--ink);
  }
</style>
</head>
<body>
<div class="flyer">
  <svg class="flyer-art" viewBox="0 0 904 1170" xmlns="http://www.w3.org/2000/svg">
    <defs>
      <linearGradient id="sky" x1="0" y1="0" x2="0" y2="1">
        <stop offset="0" stop-color="#3f7fd0"/>
        <stop offset="0.55" stop-color="#a9c9ec"/>
        <stop offset="0.8" stop-color="#e6ecf3"/>
        <stop offset="1" stop-color="#8a8f9a"/>
      </linearGradient>
      <linearGradient id="lake" x1="0" y1="0" x2="0" y2="1">
        <stop offset="0" stop-color="#b9d3ea"/>
        <stop offset="0.45" stop-color="#b07a55"/>
        <stop offset="0.75" stop-color="#4a7f5a"/>
        <stop offset="1" stop-color="#3fb6c4"/>
      </linearGradient>
      <linearGradient id="tile" x1="0" y1="0" x2="1" y2="1">
        <stop offset="0" stop-color="#3d4fae"/>
        <stop offset="1" stop-color="#7a3a9c"/>
      </linearGradient>
    </defs>

    <rect class="alpine-photo" x="0" y="0" width="904" height="520" fill="url(#sky)" role="img" aria-label="Photo of a snow-capped Alpine peak under a blue sky"/>

    <path class="corner-band" d="M0 0 H475 C400 110 230 230 0 280 Z" fill="var(--brand-purple)"/>
    <path class="corner-panel" d="M0 0 H480 C400 100 220 210 0 232 Z" fill="var(--brand-blue)"/>

    <path class="wave-purple" d="M0 390 C180 350 380 350 560 395 C700 430 820 460 904 480 V520 H0 Z" fill="var(--brand-purple)"/>
    <path class="wave-blue" d="M0 396 C180 362 380 362 560 405 C700 440 820 468 904 490 V520 H0 Z" fill="var(--brand-blue)"/>
    <path class="paper-edge" d="M0 404 C180 372 380 372 560 415 C700 450 820 478 904 506 V1170 H0 Z" fill="var(--paper)"/>
    <path class="paper-fade" d="M0 700 H904 V1170 H0 Z" fill="var(--paper-low)" opacity="0.35"/>

    <rect class="emblem-tile" x="505" y="315" width="190" height="185" rx="36" fill="url(#tile)"/>

    <path class="base-band-purple" d="M130 1170 C300 1050 560 980 904 1000 V1060 C640 1020 420 1080 240 1170 Z" fill="var(--brand-purple)"/>
    <path class="base-band-blue" d="M190 1170 C340 1075 560 1015 904 1040 V1080 C640 1050 440 1100 260 1170 Z" fill="var(--deep-blue)"/>
    <path class="lakeside-photo" d="M225 1170 C380 1070 580 1005 904 1030 V1170 Z" fill="url(#lake)" role="img" aria-label="Photo of a lakeside Swiss castle and village with mountains behind"/>
    <path class="base-band-front" d="M150 1170 C300 1070 500 1015 650 1005 C520 1030 360 1090 260 1170 Z" fill="var(--deep-blue)"/>
  </svg>

  <div class="brand">
    <span class="brand-square"></span>
    <div class="brand-name">VELMORA</div>
  </div>

  <p class="intro">The potential of the Swiss market offers many business opportunities to foreign companies, however there are some tariff and non-tariff barriers to cope with, such as its strong requirements in terms of quality and innovation, cultural and linguistic differences, specific rules applied to certain products or services.</p>

  <h1 class="headline" style="font-weight:400">Velmora is there to support you in your administrative and strategic procedures!</h1>

  <div class="body-copy">
    <p>Velmora strives to deepen the understanding of your business and acts as your local partner. We assist you in defining together all the services that best meet your needs.</p>
    <p>Our consulting skills are focused on high added value sectors, such as food and beverages, fashion &amp; lifestyle, products and services for leading industries (pharmaceutical, chemical, precision mechanics) or sustainable solutions (renewable energies, recyclable materials).</p>
    <p>From our office in Neuchate* and with our language knowledges, we are able to cover the whole of Switzerland. Having many years of experience in economic promotion and business managment, we are familiar with the Swiss trade and foreign companies wishing to export to Switzerland.</p>
  </div>

  <p class="footnote">*as of August 2020, we will open an office in Zurich as well</p>
</div>
</body>
</html>
```